The Lantern Over The Hills

This is a book about the growth of a father and how that can help us relate to our Heavenly Father. It's a Christian growth and/or self-help book, talking about experiences any father might go through, the ups and downs, the triumphs and struggles of life. Something we can all relate to.

I would prefer some artwork like the attached - showing a father with 2 or 3 kids, no faces. Something colorful and catchy.

The subhead would be:

When Little Ones Show Us How To Trust,
Rest & Walk Beside The Shepherd

By Doug Pettersen

```html
<!DOCTYPE html>
<html lang="en">
<head>
<meta charset="UTF-8">
<title>The Lantern Over The Hills — Doug Pettersen</title>
<link href="https://fonts.googleapis.com/css2?family=Cinzel:wght@500;600&family=Young+Serif&display=swap" rel="stylesheet">
<style>
  :root {
    --sky-top: #dfe3ea;
    --sky-mid: #e6e4df;
    --shirt: #e9d79a;
    --shirt-soft: #ded3b0;
    --field: #b9bf9e;
    --field-deep: #a9ae8c;
    --poppy: #d99a8c;
    --author-teal: #16899a;
    --title-white: #ffffff;
  }
  html, body {
    margin: 0;
    padding: 0;
    width: 750px;
    height: 1200px;
    overflow: hidden;
    background: #ffffff;
  }
  .cover {
    position: relative;
    width: 750px;
    height: 1200px;
    overflow: hidden;
  }
  .cover-art {
    position: absolute;
    inset: 0;
    width: 750px;
    height: 1200px;
  }
  .author {
    position: absolute;
    top: 48px;
    left: 0;
    width: 100%;
    margin: 0;
    text-align: center;
    font-family: "Cinzel", serif;
    font-weight: 600;
    font-size: 29px;
    letter-spacing: 5px;
    color: var(--author-teal);
    line-height: 1;
  }
  .title {
    position: absolute;
    top: 228px;
    left: 0;
    width: 100%;
    margin: 0;
    text-align: center;
    font-family: "Young Serif", serif;
    font-weight: 400;
    font-size: 150px;
    line-height: 142px;
    color: var(--title-white);
  }
  .title span { display: block; }
  .subtitle {
    position: absolute;
    top: 1064px;
    left: 0;
    width: 100%;
    margin: 0;
    text-align: center;
    font-family: "Cinzel", serif;
    font-weight: 500;
    font-size: 19px;
    letter-spacing: 2.4px;
    line-height: 34px;
    color: var(--title-white);
    white-space: nowrap;
  }
  .subtitle span { display: block; }
</style>
</head>
<body>
  <main class="cover">
    <svg class="cover-art" role="img" aria-label="Soft, washed-out photo of a father seen from behind carrying two young children through a meadow of red poppies under a pale sky" viewBox="0 0 750 1200" preserveAspectRatio="none">
      <defs>
        <linearGradient id="sceneGradient" x1="0" y1="0" x2="0" y2="1">
          <stop offset="0" stop-color="var(--sky-top)"/>
          <stop offset="0.25" stop-color="var(--sky-mid)"/>
          <stop offset="0.45" stop-color="var(--shirt-soft)"/>
          <stop offset="0.62" stop-color="var(--shirt)"/>
          <stop offset="0.74" stop-color="var(--field)"/>
          <stop offset="0.9" stop-color="var(--field-deep)"/>
          <stop offset="1" stop-color="var(--poppy)"/>
        </linearGradient>
      </defs>
      <rect width="750" height="1200" fill="url(#sceneGradient)"/>
    </svg>

    <p class="author">DOUG PETTERSEN</p>

    <h1 class="title">
      <span>The</span>
      <span>Lantern</span>
      <span>Over</span>
      <span>The</span>
      <span>Hills</span>
    </h1>

    <p class="subtitle">
      <span>WHEN LITTLE ONES SHOW US HOW TO TRUST,</span>
      <span>REST &amp; WALK BESIDE THE SHEPHERD</span>
    </p>
  </main>
</body>
</html>
```